Rack Card Design Project

We are a locally family owned public golf course. We would like to have a rack card designed that can be used for multiple applications. The colors in our logo are grey, blue, and white. Please use those in the card design. The company logo, contact information, address, and summer pricing should be included. I've included some pictures that may or may not be used. I'm also open to suggestions....use one photo, multiple photos, a stock photo or image representing golf etc.

```html
<!DOCTYPE html>
<html lang="en">
<head>
<meta charset="utf-8">
<title>Cedar Bend Golf Club – Summer Rates Rack Card</title>
<link href="https://fonts.googleapis.com/css2?family=Cinzel:wght@400;700&family=Roboto:wght@400;700&display=swap" rel="stylesheet">
<style>
  :root {
    --navy: #143461;
    --grey: #8e8e90;
    --grey-light: #c9cacc;
    --white: #ffffff;
    --ink: #3a3a3c;
    --page: #ffffff;
  }
  html, body { margin: 0; padding: 0; overflow: hidden; }
  body { width: 1200px; height: 1200px; background: var(--page); position: relative; }

  .rack-card {
    position: absolute; left: 347px; top: 50px;
    width: 506px; height: 1100px;
    background: var(--white);
    overflow: hidden;
    font-family: "Roboto", Arial, sans-serif;
  }
  .card-art { position: absolute; inset: 0; width: 506px; height: 1100px; }

  .season-title {
    position: absolute; left: 0; right: 0; top: 22px; margin: 0;
    text-align: center; color: var(--navy);
    font-family: "Cinzel", Georgia, serif; font-weight: 700;
    font-size: 44px; letter-spacing: 1px;
  }
  .season-dates {
    position: absolute; left: 110px; top: 84px; width: 283px; height: 33px;
    border-radius: 17px; background: var(--grey); color: var(--white);
    font-family: "Cinzel", Georgia, serif; font-size: 19px;
    display: flex; align-items: center; justify-content: center; letter-spacing: .5px;
  }
  .club-name {
    position: absolute; left: 46px; top: 366px; width: 180px; height: 80px;
    display: flex; align-items: center; justify-content: center; text-align: center;
    font-family: "Cinzel", Georgia, serif; font-weight: 700; font-size: 19px; line-height: 1.25;
    color: var(--navy);
  }

  .rates-heading {
    position: absolute; left: 28px; top: 579px; margin: 0;
    font-family: "Cinzel", Georgia, serif; font-weight: 400; font-size: 18px; color: var(--navy);
  }
  .rate-table { position: absolute; left: 28px; top: 617px; margin: 0; padding: 0; list-style: none; }
  .rate-row { display: flex; height: 25px; margin-bottom: 2.8px; }
  .rate-label {
    width: 194px; box-sizing: border-box; border: 1px solid #9a9a9c;
    padding-left: 8px; display: flex; align-items: center;
    font-size: 14px; color: var(--ink);
  }
  .rate-price {
    width: 58px; margin-left: 3px; background: var(--navy); color: var(--white);
    display: flex; align-items: center; justify-content: center; font-size: 14px;
  }

  .perks { position: absolute; left: 310px; top: 646px; margin: 0; padding: 0; list-style: none; }
  .perk { position: relative; padding-left: 14px; font-size: 14px; line-height: 18px; color: var(--ink); margin-bottom: 10px; }
  .perk::before {
    content: ""; position: absolute; left: 0; top: 6px; width: 6px; height: 6px;
    border-radius: 50%; background: var(--navy);
  }
  .perk strong { font-weight: 700; }

  .contact {
    position: absolute; left: 52px; top: 983px; color: var(--white);
    font-size: 13px; line-height: 16px;
  }
  .contact p { margin: 0 0 8px; }
</style>
</head>
<body>
  <article class="rack-card">
    <svg class="card-art" viewBox="0 0 607 1320" preserveAspectRatio="none" aria-hidden="false">
      <defs>
        <linearGradient id="heroTones" x1="0" y1="0" x2="0" y2="1">
          <stop offset="0" stop-color="#ffffff"/>
          <stop offset=".25" stop-color="#e6ddd2"/>
          <stop offset=".5" stop-color="#9b8676"/>
          <stop offset=".72" stop-color="#6f6a4a"/>
          <stop offset="1" stop-color="#8e9d56"/>
        </linearGradient>
        <linearGradient id="juniorTones" x1="0" y1="0" x2="0" y2="1">
          <stop offset="0" stop-color="#4f8fd6"/>
          <stop offset=".35" stop-color="#b9d3e6"/>
          <stop offset=".5" stop-color="#6f8f45"/>
          <stop offset="1" stop-color="#4f8a2e"/>
        </linearGradient>
        <linearGradient id="courseTones" x1="0" y1="0" x2="0" y2="1">
          <stop offset="0" stop-color="#ffffff"/>
          <stop offset=".25" stop-color="#cfd7dd"/>
          <stop offset=".45" stop-color="#ddc9a8"/>
          <stop offset=".6" stop-color="#4d5a30"/>
          <stop offset="1" stop-color="#7f9c45"/>
        </linearGradient>
        <clipPath id="heroClip">
          <path d="M0,150 H607 V560 C300,520 150,470 0,468 Z"/>
        </clipPath>
        <clipPath id="juniorClip"><circle cx="425" cy="571" r="120"/></clipPath>
      </defs>

      <g role="img" aria-label="Photo of a golfer mid-swing on a sunlit course with hills behind">
        <rect x="0" y="150" width="607" height="450" fill="url(#heroTones)" clip-path="url(#heroClip)"/>
      </g>

      <path class="wave-navy" d="M0,468 C150,470 300,520 607,560 L607,575 C400,560 200,522 0,545 Z" fill="var(--navy)"/>
      <path class="wave-grey" d="M0,545 C200,522 400,560 607,575 L607,595 C400,582 200,562 0,595 Z" fill="var(--grey)"/>

      <circle class="club-disc" cx="163" cy="488" r="113" fill="var(--grey-light)"/>

      <circle cx="425" cy="571" r="130" fill="var(--grey)"/>
      <circle cx="425" cy="571" r="124" fill="var(--navy)"/>
      <g role="img" aria-label="Photo of a young girl swinging a golf club on the fairway">
        <rect x="300" y="446" width="250" height="250" fill="url(#juniorTones)" clip-path="url(#juniorClip)"/>
      </g>

      <g role="img" aria-label="Photo of the course at sunset with tall pines and a flagstick">
        <rect x="0" y="900" width="607" height="420" fill="url(#courseTones)"/>
      </g>

      <path class="footer-grey" d="M0,1160 C130,1100 260,1100 380,1145 C470,1180 540,1228 607,1228 V1320 H0 Z" fill="var(--grey)"/>
      <path class="footer-rule" d="M0,1164 C130,1104 260,1104 380,1152 C470,1190 540,1240 607,1244" fill="none" stroke="var(--white)" stroke-width="4"/>
      <path class="footer-navy" d="M0,1170 C130,1110 260,1110 380,1160 C470,1200 540,1250 607,1255 V1320 H0 Z" fill="var(--navy)"/>
    </svg>

    <h1 class="season-title">SUMMER RATES</h1>
    <div class="season-dates">MAY 1 – SEPTEMBER 30</div>

    <div class="club-name">Cedar Bend Golf Club</div>

    <h2 class="rates-heading">18 HOLES WITH CART</h2>
    <ul class="rate-table">
      <li class="rate-row"><span class="rate-label">7AM – 11AM</span><span class="rate-price">$24</span></li>
      <li class="rate-row"><span class="rate-label">11AM – 3PM</span><span class="rate-price">$19</span></li>
      <li class="rate-row"><span class="rate-label">3PM – Close</span><span class="rate-price">$15</span></li>
      <li class="rate-row"><span class="rate-label">9 Holes With Cart</span><span class="rate-price">$15</span></li>
      <li class="rate-row"><span class="rate-label">Walking</span><span class="rate-price">$12</span></li>
    </ul>

    <ul class="perks">
      <li class="perk">Children 15 and Under<br><strong>FREE</strong> with Paid Adult</li>
      <li class="perk">Lunch Available Daily<br><strong>10AM – 3PM</strong></li>
    </ul>

    <address class="contact" style="font-style:normal">
      <p>555-014-2290<br>www.cedarbendgolf.com</p>
      <p>Cedar Bend Golf Club<br>402 Harbor Oak Rd<br>Palmview, FL 30000</p>
    </address>
  </article>
</body>
</html>
```